Coral Sleep Depot Website

Need a design for a local Miami mattress store.
The store is called Coral Sleep Depot.
need it to be something that customers can find on the internet and will
give them my location, they need to know i have the same brand mattress as the other store except i have them at almost half the price.

the office phone number is (786)555-0143
the office address is: 4127 sw Heron Bend Ave, Miami FL 33190

included is the logo, id like to stick the with white and teal design

here are is an excerpt that can or cannot be included

"We are a premium mattress discount outlet store located in South Florida; offering Free Delivery to Broward Miami-Dade, the Keys, and Palm Beach.

We carry the best brands in the market: Varnell CloudHaven; Dorvik SpineAlign, Brackett & Lowe, Pendry, among others.

We are open 7 days a week, and we are accessible from all major highways. We are a family business and our goal is to provide you with the most comfortable and best quality mattress at a price that has no competition. Come visit us and take a look at our large inventory selection."

```html
<!DOCTYPE html>
<html lang="en">
<head>
<meta charset="utf-8">
<title>Coral Sleep Depot</title>
<link rel="stylesheet" href="https://fonts.googleapis.com/css2?family=Alegreya:wght@400;500&family=Dancing+Script:wght@400;500&display=swap">
<style>
  :root {
    --teal: #1fa9cb;
    --ink: #333333;
    --muted: #8a8a8a;
    --rule: #e4e4e4;
    --tile: #3e3e3e;
    --panel: #f3fafc;
    --panel-line: #d8eef4;
    --red: #d8362b;
    --bar: #4a4a4a;
    --white: #ffffff;
  }
  * { box-sizing: border-box; margin: 0; padding: 0; }
  html, body { width: 1069px; height: 1200px; overflow: hidden; background: var(--white); }
  body { position: relative; font-family: "Alegreya", Georgia, serif; color: var(--ink); }
  a { color: inherit; text-decoration: none; }
  .abs { position: absolute; }

  /* header */
  .call { left: 143px; top: 30px; display: flex; gap: 10px; align-items: center; }
  .call-label { font-size: 11px; color: var(--muted); text-transform: uppercase; line-height: 1.1; }
  .call-number { font-size: 15px; color: var(--teal); }
  .brand { left: 384px; top: 24px; width: 300px; text-align: center; }
  .brand-mark { width: 18px; height: 18px; background: var(--teal); margin: 0 auto 8px; }
  .brand-name { font-size: 28px; color: var(--ink); line-height: 1; letter-spacing: 0.5px; }
  .locator { left: 815px; top: 26px; display: flex; gap: 10px; align-items: center; }
  .locator-text { font-size: 14px; color: var(--teal); line-height: 1.05; text-transform: uppercase; }

  .nav { left: 143px; top: 92px; width: 782px; height: 33px; border-top: 1px solid var(--rule); border-bottom: 1px solid var(--rule);
         display: flex; justify-content: space-between; align-items: center; padding: 0 12px; }
  .nav a { font-size: 12px; text-transform: uppercase; color: var(--ink); }
  .nav a.current { color: var(--teal); }

  /* hero */
  .hero { left: 143px; top: 132px; width: 583px; height: 334px;
          background: linear-gradient(135deg, #f4e3a8 0%, #e9cc7a 55%, #d9b862 100%); overflow: hidden; }
  .hero-promise { left: 42px; top: 24px; font-size: 19px; font-style: italic; color: var(--teal); line-height: 1.15; }
  .hero-promise em { color: var(--red); }
  .price-badge { left: 48px; top: 118px; width: 122px; height: 122px; border-radius: 50%; background: var(--white); text-align: center; padding-top: 22px; }
  .price-amount { color: var(--red); font-size: 40px; font-style: italic; line-height: 1; }
  .price-amount small { font-size: 13px; }
  .price-note { font-size: 14px; font-style: italic; color: var(--ink); line-height: 1.1; margin-top: 6px; }

  .tile { left: 745px; width: 180px; height: 100px; background: var(--tile); color: var(--white); }
  .tile-title { position: absolute; left: 7px; bottom: 5px; font-size: 19px; line-height: 1.05; }
  .tile-title span { color: var(--teal); }
  .tile-about { top: 132px; background: linear-gradient(160deg, #5a5a5a, #333); }
  .tile-review { top: 250px; background: linear-gradient(120deg, #2f2f2f 40%, #6a6a6a); }
  .tile-location { top: 366px; background: linear-gradient(160deg, #4d4d4d, #3a3a3a); }
  .stars { display: flex; gap: 1px; margin-top: 3px; }

  /* why */
  .why-title { left: 143px; top: 497px; width: 782px; text-align: center; font-size: 22px; }
  .why-copy { left: 200px; top: 531px; width: 668px; text-align: center; font-size: 12px; line-height: 1.6; color: #555; }
  .feature { top: 588px; width: 182px; height: 92px; background: var(--panel); border: 1px solid var(--panel-line); padding: 8px 8px; }
  .feature-head { display: flex; gap: 8px; align-items: center; height: 38px; border-bottom: 1px solid var(--panel-line); }
  .feature-title { font-size: 14px; line-height: 1.1; color: var(--ink); }
  .feature-copy { font-size: 11px; line-height: 1.6; color: #555; margin-top: 4px; }
  .feature-copy a { color: var(--teal); }

  .rule { left: 143px; width: 782px; height: 1px; background: var(--rule); }

  /* promo */
  .bed { left: 143px; top: 750px; width: 379px; height: 210px; background: linear-gradient(180deg, #f1ebe6 0%, #e7dcd3 60%, #8a4a2c 100%); }
  .promo-line { left: 546px; font-family: "Dancing Script", cursive; color: var(--ink); }
  .promo-line span { color: var(--teal); }
  .promo-red { color: var(--red); }
  .btn { left: 545px; top: 906px; width: 89px; height: 26px; border: 1px solid #555; border-radius: 2px; font-size: 12px; display: flex; align-items: center; justify-content: center; }

  /* footer */
  .foot-col { top: 1025px; width: 182px; }
  .foot-col h3 { font-size: 14px; font-weight: 400; padding-bottom: 6px; border-bottom: 1px solid var(--rule); }
  .foot-col ul { list-style: none; margin-top: 9px; }
  .foot-col li { font-size: 11px; color: var(--muted); line-height: 17.5px; }
  .foot-col p { font-size: 11px; color: var(--muted); line-height: 1.55; margin-top: 9px; }
  .signup { margin-top: 8px; height: 24px; border: 1px solid var(--rule); border-radius: 3px; display: flex; align-items: center; justify-content: space-between; padding: 0 8px; font-size: 11px; color: var(--muted); }
  .bottom-bar { left: 0; top: 1156px; width: 1069px; height: 44px; background: var(--bar); }
  .copyright { left: 143px; top: 16px; font-size: 10px; color: #d6d6d6; }
  .social { right: 144px; top: 15px; display: flex; gap: 12px; }
  .social i { display: block; width: 13px; height: 13px; border-radius: 50%; background: #e6e6e6; }
</style>
</head>
<body>

<header>
  <div class="abs call">
    <svg width="30" height="30" viewBox="0 0 30 30" aria-hidden="true"><circle cx="15" cy="15" r="13.5" fill="none" stroke="#9a9a9a" stroke-width="1.6"/><path d="M10 8c-1 1-1.5 3 0 6s4 6 7 7.5c2 1 3.5.5 4.5-.5l-2.5-2.5-2 1c-1.5-.8-3.5-2.8-4.3-4.3l1-2z" fill="#9a9a9a"/></svg>
    <div><div class="call-label">Call us</div><div class="call-number">(786)555-0143</div></div>
  </div>
  <div class="abs brand">
    <div class="brand-mark"></div>
    <div class="brand-name">Coral Sleep Depot</div>
  </div>
  <div class="abs locator">
    <svg width="34" height="34" viewBox="0 0 34 34" aria-hidden="true"><circle cx="17" cy="17" r="10" fill="none" stroke="#9a9a9a" stroke-width="1.8"/><path d="M17 2v8M17 24v8M2 17h8M24 17h8" stroke="#9a9a9a" stroke-width="1.8"/><circle cx="17" cy="17" r="3" fill="#9a9a9a"/></svg>
    <div class="locator-text">Store<br>Locator</div>
  </div>
  <nav class="abs nav">
    <a class="current" href="#">Home</a>
    <a href="#">Brand &amp; Price</a>
    <a href="#">Mattress &amp; Product</a>
    <a href="#">Special Offer</a>
    <a href="#">FAQ</a>
    <a href="#">Contact Us</a>
  </nav>
</header>

<section class="abs hero" role="img" aria-label="Sunlit bedroom with a large cushioned bed and a lake view through the window">
  <p class="abs hero-promise">Not just a low price guarantee,<br>but we guarantee the lowest price or<br>it's <em>FREE!</em></p>
  <div class="abs price-badge">
    <div class="price-amount"><small>Only $</small>999</div>
    <div class="price-note">Lowest Price<br>Gurantee</div>
  </div>
</section>

<a class="abs tile tile-about" href="#" role="img" aria-label="Showroom with mattresses on display"><span class="tile-title">About <span>Outlet</span></span></a>
<a class="abs tile tile-review" href="#" role="img" aria-label="Customer resting on a mattress"><span class="tile-title">Customer<br><span>Review</span>
  <span class="stars">
    <svg width="70" height="12" viewBox="0 0 70 12" aria-hidden="true"><g fill="#f4c21c"><path id="s" d="M6 0l1.8 3.9 4.2.4-3.2 2.8 1 4.1L6 9 2.2 11.2l1-4.1L0 4.3l4.2-.4z"/><use href="#s" x="14"/><use href="#s" x="28"/><use href="#s" x="42"/><use href="#s" x="56"/></g></svg>
  </span></span></a>
<a class="abs tile tile-location" href="#" role="img" aria-label="Street map showing the store location"><span class="tile-title">Find a<br><span>Location</span></span></a>

<section>
  <h2 class="abs why-title" style="font-weight:400">Why Choose Coral Sleep Depot</h2>
  <p class="abs why-copy">We also have outstanding customer service ratings that prove we are the top mattress outlet that meets your budget and know how to deliver on the promises we make to ensure you a quality good night sleep.</p>

  <div class="abs feature" style="left:143px">
    <div class="feature-head">
      <svg width="26" height="26" viewBox="0 0 26 26" aria-hidden="true"><circle cx="13" cy="13" r="12" fill="none" stroke="var(--teal)" stroke-width="2"/><path d="M7 13.5l4 4 8-8.5" fill="none" stroke="var(--teal)" stroke-width="2.4"/></svg>
      <div class="feature-title">100% Satisfaction<br>Guarantee</div>
    </div>
    <p class="feature-copy">Low price, variety &amp; quality mattresses. <a href="#">Read more...</a></p>
  </div>
  <div class="abs feature" style="left:343px">
    <div class="feature-head">
      <svg width="30" height="26" viewBox="0 0 30 26" aria-hidden="true"><path d="M2 8l10-6 16 6-4 16-18-4z" fill="var(--teal)"/><circle cx="9" cy="8" r="2" fill="#fff"/></svg>
      <div class="feature-title">Cheapest Prices<br>Guarantee</div>
    </div>
    <p class="feature-copy">Outlet smart &amp; save. Shop Coral Sleep Depot. <a href="#">Read more...</a></p>
  </div>
  <div class="abs feature" style="left:544px">
    <div class="feature-head">
      <svg width="32" height="26" viewBox="0 0 32 26" aria-hidden="true"><ellipse cx="16" cy="14" rx="12" ry="9" fill="none" stroke="var(--teal)" stroke-width="2"/><path d="M12 18l8-8" stroke="var(--teal)" stroke-width="1.8"/><circle cx="12.5" cy="11" r="1.6" fill="var(--teal)"/><circle cx="19.5" cy="17" r="1.6" fill="var(--teal)"/></svg>
      <div class="feature-title">Interest Free<br>Financing</div>
    </div>
    <p class="feature-copy">90 Days payment option with 0% intrest. <a href="#">Read more...</a></p>
  </div>
  <div class="abs feature" style="left:744px">
    <div class="feature-head">
      <svg width="34" height="26" viewBox="0 0 34 26" aria-hidden="true"><rect x="1" y="7" width="20" height="12" fill="var(--teal)"/><path d="M21 10h7l4 5v4H21z" fill="var(--teal)"/><circle cx="7" cy="21" r="3" fill="#fff" stroke="var(--teal)" stroke-width="2"/><circle cx="26" cy="21" r="3" fill="#fff" stroke="var(--teal)" stroke-width="2"/><circle cx="24" cy="5" r="4" fill="none" stroke="var(--teal)" stroke-width="1.5"/></svg>
      <div class="feature-title">Same Day Delivery<br>&amp; Setup</div>
    </div>
    <p class="feature-copy">Free Delivery with safe and secure mattress &amp; setup. <a href="#">Read more...</a></p>
  </div>
</section>

<div class="abs rule" style="top:714px"></div>

<section>
  <div class="abs bed" role="img" aria-label="Wooden bed frame with a white mattress and floating pillows"></div>
  <p class="abs promo-line" style="top:756px;font-size:21px"><span>5 Factors</span> to consider when shopping</p>
  <p class="abs promo-line" style="top:786px;font-size:27px">Coral Sleep Depot <span>Brand</span> with</p>
  <p class="abs promo-line promo-red" style="top:819px;font-size:19px">Low price just got lower</p>
  <p class="abs promo-line promo-red" style="top:862px;font-size:22px;font-family:'Alegreya',serif;font-style:italic">Find the perfect mattress here</p>
  <a class="abs btn" href="#">Find a Store</a>
</section>

<div class="abs rule" style="top:994px"></div>

<footer>
  <div class="abs foot-col" style="left:143px">
    <h3>Our Product</h3>
    <ul><li>Mattresses</li><li>Foundations</li><li>Pillows</li><li>Accessories</li></ul>
  </div>
  <div class="abs foot-col" style="left:343px">
    <h3>Our Outlet</h3>
    <ul><li>About Us</li><li>5 Factors</li><li>Why Coral Sleep Depot</li><li>Mattress Technology</li></ul>
  </div>
  <div class="abs foot-col" style="left:544px">
    <h3>Customer Service</h3>
    <ul><li>Warranty Information</li><li>Where to Shop</li><li>FAQs</li><li>Coral Sleep Depot Facts</li></ul>
  </div>
  <div class="abs foot-col" style="left:744px">
    <h3>Newsletter Subscription</h3>
    <p>Subscribe to our email newsletter for latest offer &amp; discount on mattress.</p>
    <div class="signup"><span>Email address...</span>
      <svg width="12" height="10" viewBox="0 0 12 10" aria-hidden="true"><path d="M1 1l4 4-4 4M6 1l4 4-4 4" fill="none" stroke="var(--teal)" stroke-width="1.6"/></svg>
    </div>
  </div>
  <div class="abs bottom-bar">
    <p class="abs copyright">©2014 Coral Sleep Depot. All Rights Reserved.</p>
    <div class="abs social" aria-label="Social links"><i></i><i></i><i></i><i></i><i></i></div>
  </div>
</footer>

</body>
</html>
```